Business cards - KESTO Roofing & Siding

We need simple business cards made up for our Roofing & Siding business based in Calgary Alberta.
The logo on one side of the card and potentially our slogan "Built with trust, verified by time".
The other side could have:
-A small logo
-Rep name:
-Rep cell phone:
-Rep email:
-Office phone: 403-386-2049
-Website: PrairieShinglePros.com

We would like to incorporate the colours from our logo, especially the lite blue on the jpeg file. I have attached the ai file and jpeg file. We like the colours better on the jpeg file.

I do not require a money back guarantee

```html
<!DOCTYPE html>
<html lang="en">
<head>
<meta charset="utf-8">
<title>KESTO Roofing &amp; Siding — Business Cards</title>
<link rel="stylesheet" href="https://fonts.googleapis.com/css2?family=Arimo:wght@400;700&display=swap">
<style>
  :root {
    --stage: #e4e4e2;
    --card-white: #ffffff;
    --brand-blue: #0b6bb5;
    --brand-blue-light: #4a8fd4;
    --brand-blue-pale: #e9f0f8;
    --brand-red: #e31e25;
    --ink: #2a2a2a;
    --ink-soft: #6b6b6b;
  }
  * { box-sizing: border-box; margin: 0; padding: 0; }
  html, body {
    width: 1200px; height: 801px; overflow: hidden;
    background: var(--stage);
    font-family: "Arimo", Arial, sans-serif;
  }
  .stage {
    position: relative; width: 1200px; height: 801px;
    display: flex; align-items: center; justify-content: center; gap: 56px;
  }
  .card {
    position: relative; width: 520px; height: 298px; overflow: hidden;
    box-shadow: 0 10px 26px rgba(0,0,0,.18);
  }

  /* ---------- front (contact side) ---------- */
  .card--front { background: var(--card-white); }
  .card--front .edge-band {
    position: absolute; left: 0; right: 0; bottom: 0; height: 9px; display: flex;
  }
  .edge-band .edge-band__blue { flex: 62; background: var(--brand-blue-light); }
  .edge-band .edge-band__gap { flex: 1; background: var(--card-white); }
  .edge-band .edge-band__red { flex: 37; background: var(--brand-red); }

  .rep {
    position: absolute; top: 30px; right: 32px; text-align: right;
  }
  .rep__name {
    color: var(--brand-red); font-weight: 700; font-size: 19px; letter-spacing: .2px;
  }
  .rep__title { color: var(--ink-soft); font-size: 14px; margin-top: 3px; }

  .wordmark {
    position: absolute; left: 34px; top: 100px;
    display: flex; align-items: center; gap: 12px;
  }
  .wordmark__square { width: 22px; height: 22px; background: var(--brand-blue); }
  .wordmark__name {
    font-weight: 700; font-size: 25px; letter-spacing: 2px; color: var(--brand-blue);
  }
  .wordmark__est {
    position: absolute; left: 68px; top: 76px;
    font-size: 11px; letter-spacing: 2px; color: var(--ink);
  }

  .contacts {
    position: absolute; left: 34px; bottom: 30px; list-style: none;
  }
  .contacts li {
    display: flex; align-items: center; gap: 10px;
    font-size: 15px; color: var(--ink); line-height: 24px;
  }
  .contacts svg { width: 15px; height: 15px; flex: none; }

  /* ---------- back (brand side) ---------- */
  .card--back {
    background: linear-gradient(160deg, var(--brand-blue) 0%, var(--brand-blue) 55%, #0a5a9b 100%);
  }
  .card--back .brand-lockup {
    position: absolute; left: 0; right: 0; top: 104px; text-align: center; color: #fff;
  }
  .brand-lockup__est { font-size: 12px; letter-spacing: 3px; margin-bottom: 12px; }
  .brand-lockup__row { display: inline-flex; align-items: center; gap: 14px; }
  .brand-lockup__square { width: 26px; height: 26px; background: #fff; }
  .brand-lockup__name { font-weight: 700; font-size: 31px; letter-spacing: 3px; }
</style>
</head>
<body>
<main class="stage">

  <section class="card card--front" aria-label="Business card, contact side">
    <div class="rep">
      <p class="rep__name">DANIEL MOREAU</p>
      <p class="rep__title">Manager</p>
    </div>

    <div class="wordmark">
      <span class="wordmark__square"></span>
      <span class="wordmark__name">KESTO Roofing &amp; Siding</span>
    </div>
    <p class="wordmark__est">Est. 1991</p>

    <ul class="contacts">
      <li>
        <svg viewBox="0 0 16 16" aria-hidden="true"><rect x="4" y="1" width="8" height="14" rx="1.5" fill="none" stroke="#e31e25" stroke-width="1.6"/><circle cx="8" cy="12.3" r=".9" fill="#e31e25"/></svg>
        403-386-2049
      </li>
      <li>
        <svg viewBox="0 0 16 16" aria-hidden="true"><path d="M3 2.5l3 .2 1 3-1.8 1.3a9 9 0 0 0 3.8 3.8L10.3 9l3 1 .2 3c-6 .8-11.3-4.5-10.5-10.5z" fill="#e31e25"/></svg>
        403-386-2049
      </li>
      <li>
        <svg viewBox="0 0 16 16" aria-hidden="true"><rect x="1" y="3.5" width="14" height="9.5" fill="#e31e25"/><path d="M1.5 4l6.5 5 6.5-5" fill="none" stroke="#fff" stroke-width="1.2"/></svg>
        info@PrairieShinglePros.com
      </li>
      <li>
        <svg viewBox="0 0 16 16" aria-hidden="true"><circle cx="8" cy="8" r="6.5" fill="none" stroke="#e31e25" stroke-width="1.6"/><path d="M1.5 8h13M8 1.5c-3 3.5-3 9.5 0 13M8 1.5c3 3.5 3 9.5 0 13" fill="none" stroke="#e31e25" stroke-width="1.2"/></svg>
        PrairieShinglePros.com
      </li>
    </ul>

    <div class="edge-band">
      <span class="edge-band__blue"></span><span class="edge-band__gap"></span><span class="edge-band__red"></span>
    </div>
  </section>

  <section class="card card--back" aria-label="Business card, brand side">
    <div class="brand-lockup">
      <p class="brand-lockup__est">Est. 1991</p>
      <div class="brand-lockup__row">
        <span class="brand-lockup__square"></span>
        <span class="brand-lockup__name">KESTO Roofing &amp; Siding</span>
      </div>
    </div>
  </section>

</main>
</body>
</html>
```